Web Design For Metal Recycling Company

We are a scrap and recycling company dealing mainly in scrap metal base in Singapore. We deal in both domestic market and international market. Currently we are still unsure if we want to have a "lively" or "professional" company image so we will leave it to the designer to deem what is good.

We wish for a website to be able to "Retain" the interest of new visitor and at the same time able to give enough information for new and existing customer. We would also wish for design that will get the visitor to "Engage" us.

The attached is the logo for the company and we would want to incorporate that into the website. Either of the logo is fine.

```html
<!DOCTYPE html>
<html lang="en">
<head>
<meta charset="utf-8">
<title>Tan Keng Metals – Home</title>
<link href="https://fonts.googleapis.com/css2?family=Montserrat:wght@400;600;700;800&family=Lato:wght@400;700&display=swap" rel="stylesheet">
<style>
:root{
  --gold:#d4940a;
  --gold-card:#d09000;
  --ink:#222;
  --text:#444;
  --white:#fff;
  --card-bg:#f0f0f0;
  --card-line:#dcdcdc;
  --footer-band:#2b2009;
  --footer-body:#1d1507;
  --footer-base:#150f04;
  --footer-text:#8a7f6c;
  --footer-line:#3a2f1a;
}
*{margin:0;padding:0;box-sizing:border-box}
html,body{width:1098px;height:1200px;overflow:hidden;background:var(--white)}
body{position:relative;font-family:"Lato",sans-serif;color:var(--text)}
.abs{position:absolute}

/* hero */
.hero{left:0;top:0;width:1098px;height:420px;
  background:radial-gradient(ellipse at 35% 60%,#5a2a14 0%,#3a1e12 40%,#1e1410 100%)}
.site-header{left:0;top:0;width:1098px;height:60px;background:rgba(10,8,6,.72)}
.brand{left:102px;top:11px;display:flex;align-items:center;gap:9px}
.brand-mark{width:38px;height:38px;border:2px solid var(--gold)}
.brand-name{font-family:"Montserrat",sans-serif;font-weight:700;font-size:16px;color:var(--gold);letter-spacing:1px}
.main-nav{right:10px;top:22px;display:flex;gap:0;font-family:"Montserrat",sans-serif;font-size:11.5px}
.main-nav a{color:#ddd;text-decoration:none;margin-left:36px}
.main-nav a.active{color:var(--gold)}
.hero-title{left:101px;top:130px;font-family:"Montserrat",sans-serif;font-weight:800;font-size:34px;color:var(--white);letter-spacing:-.5px}
.hero-title em{font-style:normal;color:var(--gold)}
.hero-text{left:102px;top:187px;width:655px;font-family:"Montserrat",sans-serif;font-size:12.3px;line-height:16px;color:var(--white)}
.btn-light{left:102px;top:263px;width:128px;height:38px;background:var(--white);color:var(--ink);
  font-family:"Montserrat",sans-serif;font-weight:700;font-size:12px;display:flex;align-items:center;justify-content:center}
.dots{left:519px;top:389px;display:flex;gap:8px}
.dots span{width:12px;height:12px;border-radius:50%;background:#ccc}
.dots span.current{background:transparent;border:1.5px solid #ddd}

/* services */
.section-title{left:0;top:470px;width:1098px;text-align:center;font-family:"Montserrat",sans-serif;font-weight:700;font-size:21px;color:var(--ink)}
.section-text{left:190px;top:511px;width:718px;text-align:center;font-size:10.5px;line-height:14px;color:#555}
.card{top:583px;width:234px;height:305px;background:var(--card-bg);border:1px solid var(--card-line);text-align:center}
.card.featured{background:var(--gold-card);border-color:var(--gold-card)}
.card .photo{position:absolute;left:50px;top:21px;width:134px;height:134px;border-radius:50%;border:4px solid #d8d8d8}
.card.featured .photo{border-color:#f2d9a0}
.card h3{position:absolute;left:0;top:168px;width:100%;font-family:"Montserrat",sans-serif;font-weight:700;font-size:12.5px;color:var(--gold)}
.card.featured h3{color:var(--white)}
.card p{position:absolute;left:12px;top:198px;width:210px;font-size:10.5px;line-height:12.5px;color:#333}
.card.featured p{color:var(--white)}
.card .btn-quote{position:absolute;left:67px;top:251px;width:100px;height:34px;background:var(--gold);border:1px solid #b97f00;color:var(--white);
  font-family:"Montserrat",sans-serif;font-weight:700;font-size:11px;display:flex;align-items:center;justify-content:center}
.card.featured .btn-quote{background:var(--white);color:var(--ink);border-color:var(--white)}

/* footer */
.footer-nav{left:0;top:935px;width:1098px;height:41px;background:var(--footer-band)}
.footer-nav a{position:absolute;top:0;height:41px;display:flex;align-items:center;justify-content:center;
  border-left:1px solid var(--footer-line);font-size:11.5px;color:var(--footer-text);text-decoration:none}
.footer-nav a.last{border-right:1px solid var(--footer-line)}
.footer-body{left:0;top:976px;width:1098px;height:184px;background:var(--footer-body)}
.footer-col{top:994px;font-size:10px;color:var(--footer-text)}
.footer-col h4{font-weight:400;font-size:12px;color:#9a8f7b;padding-bottom:8px;border-bottom:1px solid var(--footer-line);margin-bottom:8px}
.footer-col li{list-style:none;line-height:20.5px}
.contact li{display:flex;gap:6px;align-items:flex-start;line-height:13px;margin-bottom:7.5px}
.contact svg{flex:none;margin-top:1px}
.subscribe{display:flex;margin-top:14px}
.subscribe .field{width:166px;height:26px;background:#f4f4f4;color:#b8a27a;font-size:10px;display:flex;align-items:center;padding-left:10px}
.subscribe .go{width:35px;height:26px;background:var(--gold);color:var(--white);font-weight:700;font-size:11px;display:flex;align-items:center;justify-content:center}
.social li{display:flex;align-items:center;gap:9px}
.social i{width:15px;height:15px;border-radius:50%;background:#3b3224;display:inline-block}
.copyright{left:0;top:1160px;width:1098px;height:40px;background:var(--footer-base);color:#4a3f2c;font-size:9.5px;display:flex;align-items:center;justify-content:center}
</style>
</head>
<body>

<div class="abs hero" role="img" aria-label="Photo of a heap of rusted scrap metal parts"></div>

<header class="abs site-header">
  <div class="abs brand"><span class="brand-mark"></span><span class="brand-name">TAN KENG METALS</span></div>
  <nav class="abs main-nav">
    <a class="active">Home</a><a>About</a><a>Services</a><a>Metal Prices</a><a>Recycling</a><a>News</a><a>Contact Us</a>
  </nav>
</header>

<h1 class="abs hero-title">EXPERIENCED . <em>RELIABLE</em> . AFFORDABLE</h1>
<p class="abs hero-text">Sed ut perspiciatis unde omnis iste natus error sit voluptatem accusantium doloremque laudantium, totam rem aperiam, eaque ipsa quae ab illo inventore veritatis et quasi architecto beatae vitae dicta sunt explicabo. Nemo enim ipsam voluptatem quia voluptas.</p>
<a class="abs btn-light">KNOW MORE</a>
<div class="abs dots"><span class="current"></span><span></span><span></span></div>

<h2 class="abs section-title">PROVIDING RELIABLE RECYCLING</h2>
<p class="abs section-text">Lorem ipsum dolor sit amet, consectetur adipisicing elit, sed do eiusmod tempor incididunt ut labore et dolore magna aliqua. Ut enim ad minim veniam, quis nostrud exercitation ullamco laboris nisi ut aliquip ex ea commodo consequat. Duis aute irure dolor in reprehenderit in voluptate velit esse cillum dolore eu fugiat nulla pariatur.</p>

<article class="abs card" style="left:173px">
  <div class="photo" role="img" aria-label="Photo of a crane grab over a scrap metal pile under blue sky" style="background:linear-gradient(180deg,#3f8fd8 0%,#5aa6e6 55%,#7a4a2a 75%,#4a2e1c 100%)"></div>
  <h3>SCRAP METAL RECYCLING</h3>
  <p>At vero eos et accusamus et iusto odio dignissimos atque corrupti quos dolores et qumolestiaaecati cupiditat</p>
  <a class="btn-quote">GET QUOTE</a>
</article>

<article class="abs card featured" style="left:433px">
  <div class="photo" role="img" aria-label="Photo of a pile of crushed scrap cars" style="background:radial-gradient(circle at 50% 45%,#7a4a30 0%,#4a3428 50%,#2a2a30 100%)"></div>
  <h3>SCRAP CAR RECYCLING</h3>
  <p>At vero eos et accusamus et iusto odio dignissimos atque corrupti quos dolores et qumolestiaaecati cupiditat</p>
  <a class="btn-quote">GET QUOTE</a>
</article>

<article class="abs card" style="left:691px">
  <div class="photo" role="img" aria-label="Photo of a green skip bin against a white brick wall" style="background:linear-gradient(180deg,#c8d4e0 0%,#b6c2cc 45%,#2f6a48 60%,#24553a 100%)"></div>
  <h3>AFFORDABLE SKIP HIRE</h3>
  <p>At vero eos et accusamus et iusto odio dignissimos atque corrupti quos dolores et qumolestiaaecati cupiditat</p>
  <a class="btn-quote">GET QUOTE</a>
</article>

<nav class="abs footer-nav">
  <a style="left:102px;width:103px">Home</a>
  <a style="left:205px;width:104px">About</a>
  <a style="left:309px;width:114px">Services</a>
  <a style="left:423px;width:139px">Metal Prices</a>
  <a style="left:562px;width:118px">Recycling</a>
  <a style="left:680px;width:101px">News</a>
  <a style="left:781px;width:92px">Login</a>
  <a class="last" style="left:873px;width:121px">Contact Us</a>
</nav>

<div class="abs footer-body"></div>

<div class="abs footer-col" style="left:102px;width:128px">
  <h4>Usefull Links</h4>
  <ul><li>Lorem Ipsum</li><li>Dolor Elit</li><li>Magna</li><li>Consecturae</li><li>Lorem</li></ul>
</div>

<div class="abs footer-col contact" style="left:297px;width:250px">
  <h4 style="width:130px">Contact Us</h4>
  <ul>
    <li><svg width="11" height="12" viewBox="0 0 11 12"><path d="M5.5 11.5C5.5 11.5 1 7 1 4.5a4.5 4.5 0 0 1 9 0C10 7 5.5 11.5 5.5 11.5z" fill="none" stroke="#6f6553"/><circle cx="5.5" cy="4.5" r="1.5" fill="none" stroke="#6f6553"/></svg><span>Location : 48 Harbour Rd. 2nd Floor Westvale, IL 60418</span></li>
    <li><svg width="11" height="9" viewBox="0 0 11 9"><rect x=".5" y=".5" width="10" height="8" fill="none" stroke="#6f6553"/><path d="M.5.5l5 4 5-4" fill="none" stroke="#6f6553"/></svg><span>Email : tankengmetals.com</span></li>
    <li><svg width="11" height="11" viewBox="0 0 11 11"><path d="M2 1l2 2-1 1.5c.8 1.6 2 2.8 3.5 3.5L8 7l2 2-1.5 1.5C5 10 1 6 .5 2.5z" fill="none" stroke="#6f6553"/></svg><span>Phone : 555 . 204 . 3187</span></li>
    <li><svg width="11" height="11" viewBox="0 0 11 11"><rect x="1.5" y=".5" width="8" height="10" fill="none" stroke="#6f6553"/><path d="M3 3.5h5M3 5.5h5M3 7.5h3" stroke="#6f6553"/></svg><span>Fax : 555 . 204 . 3190</span></li>
  </ul>
</div>

<div class="abs footer-col" style="left:615px;width:205px">
  <h4 style="width:127px">Join Us Now !</h4>
  <p style="line-height:14px">Subscribe to our e-mail newsletter to receive updates !</p>
  <div class="subscribe"><span class="field">Enter your email</span><span class="go">Go !</span></div>
</div>

<div class="abs footer-col social" style="left:867px;width:127px">
  <h4>Follow Us On</h4>
  <ul><li><i></i>Friendlane</li><li><i></i>Pinboardly</li><li><i></i>Searchly +</li><li><i></i>Vidstream</li></ul>
</div>

<div class="abs copyright">Copyright © 2014 . TAN KENG METALS ®. All Rights Reserved .</div>

</body>
</html>
```